Your complete Gardening and lawn maintenance, Horticultural care. (to be on card)
We are looking at using a logo of a tree, with a recycling emblem circling the tree. The colors of choice, are burnt oranges and olive greens. Presented; simple to the eye, yet catchy to the clients in a eco-friendly way. We have uploaded a design for you to look at just to give a rough idea, you can use that or create your own ideas or play around with a mixture.

Target Market(s)

Home owners, businesses, real estates.

Industry/Entity Type

Recycling

Contact Information for Business Card

Name: Derek Ostrowe
Phone: 0421583906
Email: bramblewoodyards@mailnest.net

Logo Text

Bramble-Wood Yards

Logo styles of interest
Emblem Logo
Pictorial/Combination Logo
Abstract Logo
Requirements
Must have
• Business name: Bramble-Wood Yards
and slogan : Your complete Gardening and lawn maintenance, Horticultural care

```html
<!DOCTYPE html>
<html lang="en">
<head>
<meta charset="UTF-8">
<title>Bramble-Wood Yards – Business Card</title>
<link href="https://fonts.googleapis.com/css2?family=Bree+Serif&family=Arimo:wght@400;700&display=swap" rel="stylesheet">
<style>
  :root {
    --page-bg: #f2f2f0;
    --card-light: #ffffff;
    --card-mint: #d9ebcb;
    --olive-green: #2f7a2f;
    --burnt-orange: #f07c1b;
    --text-green: #2e6e2c;
    --text-dark: #3a3a3a;
  }
  * { margin: 0; padding: 0; box-sizing: border-box; }
  html, body {
    width: 1200px;
    height: 900px;
    overflow: hidden;
    background: var(--page-bg);
  }
  .business-card {
    position: absolute;
    left: 100px;
    top: 150px;
    width: 1000px;
    height: 600px;
    border-radius: 36px;
    overflow: hidden;
    background: linear-gradient(180deg, var(--card-mint) 0%, var(--card-light) 45%, var(--card-mint) 100%);
    box-shadow: 0 10px 30px rgba(0, 0, 0, 0.12);
  }
  .card-waves {
    position: absolute;
    inset: 0;
    width: 100%;
    height: 100%;
  }
  .holder-name {
    position: absolute;
    right: 70px;
    top: 48px;
    font-family: 'Arimo', sans-serif;
    font-size: 26px;
    color: var(--burnt-orange);
  }
  .brand-mark {
    position: absolute;
    left: 430px;
    top: 118px;
    width: 140px;
    height: 140px;
    border-radius: 50%;
    background: var(--olive-green);
  }
  .brand-name {
    position: absolute;
    left: 0;
    width: 100%;
    top: 278px;
    text-align: center;
    font-family: 'Bree Serif', serif;
    font-size: 70px;
    line-height: 1;
    color: var(--olive-green);
  }
  .brand-tagline {
    position: absolute;
    left: 0;
    width: 100%;
    top: 362px;
    text-align: center;
    font-family: 'Arimo', sans-serif;
    font-weight: 700;
    font-size: 19px;
    color: var(--text-green);
  }
  .contact-list {
    position: absolute;
    left: 70px;
    top: 428px;
    list-style: none;
    font-family: 'Arimo', sans-serif;
    font-size: 31px;
    color: var(--text-dark);
  }
  .contact-item {
    display: flex;
    align-items: center;
    gap: 8px;
    height: 44px;
  }
  .contact-icon {
    width: 30px;
    height: 30px;
    flex: none;
  }
</style>
</head>
<body>
  <div class="business-card">
    <svg class="card-waves" viewBox="0 0 1000 600" preserveAspectRatio="none" aria-hidden="true">
      <path d="M0,0 H650 C430,25 210,80 0,220 Z" fill="var(--olive-green)"/>
      <path d="M0,0 H360 C230,25 100,70 0,150 Z" fill="var(--burnt-orange)"/>
      <path d="M1000,300 C930,410 780,520 560,600 H1000 Z" fill="var(--burnt-orange)"/>
      <path d="M1000,440 C880,530 650,560 250,600 H1000 Z" fill="var(--olive-green)"/>
    </svg>

    <p class="holder-name">Derek Ostrowe</p>

    <div class="brand-mark"></div>
    <h1 class="brand-name">Bramble-Wood Yards</h1>
    <p class="brand-tagline">Your complete Gardening and lawn maintenance, Horticultural care</p>

    <ul class="contact-list">
      <li class="contact-item">
        <svg class="contact-icon" viewBox="0 0 24 24" aria-hidden="true">
          <path d="M6.6 10.8c1.4 2.8 3.8 5.1 6.6 6.6l2.2-2.2c.3-.3.7-.4 1-.2 1.1.4 2.3.6 3.6.6.6 0 1 .4 1 1V20c0 .6-.4 1-1 1C10.6 21 3 13.4 3 4c0-.6.4-1 1-1h3.5c.6 0 1 .4 1 1 0 1.3.2 2.5.6 3.6.1.3 0 .7-.2 1z" fill="var(--burnt-orange)"/>
        </svg>
        <span class="contact-phone">0421583906</span>
      </li>
      <li class="contact-item">
        <svg class="contact-icon" viewBox="0 0 24 24" aria-hidden="true">
          <rect x="2" y="5" width="20" height="14" rx="2" fill="var(--burnt-orange)"/>
          <path d="M3 6l9 7 9-7" fill="none" stroke="#ffffff" stroke-width="1.8"/>
        </svg>
        <span class="contact-email">bramblewoodyards@mailnest.net</span>
      </li>
    </ul>
  </div>
</body>
</html>
```